Postcard Design

www.tovil.com.au
i am an occupational therapist and professionally trained coach. i work with children, parents and disability service providers to achieve brilliant outcomes for children with special needs.
http://www.tovil.com.au/service/for-families
I need a postcard to give parents to promote our family service coaching service
A family service coach will work with you to set specific goals for your child, build a dream team, design and manage your child's highly effective therapy and educational team to ensure brilliant outcomes for your child..
KORBU - you have done my business card previously. they were great thank you.

```html
<!DOCTYPE html>
<html lang="en">
<head>
<meta charset="utf-8">
<title>Tovil Consulting – Postcard</title>
<link rel="stylesheet" href="https://fonts.googleapis.com/css2?family=Arimo:ital,wght@0,400;0,700;1,700&display=swap">
<style>
  :root {
    --paper: #ffffff;
    --header-grey-light: #c9d1d6;
    --header-grey-dark: #8e9aa3;
    --panel-blue: #2461a5;
    --panel-blue-light: #3f74b4;
    --wave-navy: #283f92;
    --text-white: #ffffff;
    --rule-grey: #555a60;
    --stamp-line: #333333;
    --decor-faint: #eef2f8;
  }
  * { margin: 0; padding: 0; box-sizing: border-box; }
  html, body {
    width: 1200px; height: 924px; overflow: hidden;
    background: var(--paper);
    font-family: "Arimo", Arial, sans-serif;
  }
  .postcard { position: relative; width: 1200px; height: 924px; background: var(--paper); }

  .about-side { position: absolute; left: 0; top: 0; width: 607px; height: 818px; overflow: hidden; }
  .about-art { position: absolute; inset: 0; }

  .section-label {
    position: absolute; left: 38px; top: 32px;
    font-size: 25px; font-weight: 400; color: var(--text-white);
  }
  .profile-name {
    position: absolute; left: 35px; top: 123px;
    font-size: 47px; font-weight: 700; color: var(--text-white); letter-spacing: -0.5px;
  }
  .profile-roles {
    position: absolute; left: 62px; top: 187px; list-style: none;
    font-size: 20px; line-height: 21.5px; color: var(--text-white); font-weight: 400;
  }
  .role-marker {
    position: absolute; left: 39px; top: 182px; width: 10px; height: 70px;
  }
  .role-marker::before {
    content: ""; position: absolute; left: 0; top: 0; width: 9px; height: 9px;
    border-radius: 50%; background: var(--text-white);
  }
  .role-marker::after {
    content: ""; position: absolute; left: 4px; top: 6px; width: 1.5px; height: 64px;
    background: var(--text-white);
  }

  .bio {
    position: absolute; left: 43px; top: 373px; width: 550px;
    font-size: 22.4px; line-height: 30.5px; color: var(--text-white);
  }
  .invitation {
    position: absolute; left: 46px; top: 698px; width: 550px;
    font-size: 22px; line-height: 30.5px; font-weight: 700; font-style: italic;
    color: var(--text-white);
  }

  .address-side { position: absolute; left: 607px; top: 0; width: 593px; height: 924px; }
  .decor { position: absolute; left: 0; top: 0; }
  .stamp-box {
    position: absolute; left: 405px; top: 59px; width: 148px; height: 167px;
    border: 1.3px solid var(--stamp-line); background: var(--paper);
  }
  .address-line {
    position: absolute; left: 136px; width: 398px; height: 0;
    border-top: 1.3px solid var(--rule-grey);
  }
  .address-line.l1 { top: 405px; }
  .address-line.l2 { top: 501px; }
  .address-line.l3 { top: 597px; }
</style>
</head>
<body>
<main class="postcard">
  <section class="about-side">
    <svg class="about-art" width="607" height="818" viewBox="0 0 607 818">
      <defs>
        <linearGradient id="headerGrey" x1="0" y1="0" x2="1" y2="0.3">
          <stop offset="0" stop-color="#a9b4bb"/>
          <stop offset="0.6" stop-color="#cdd4d8"/>
          <stop offset="1" stop-color="#9aa6ae"/>
        </linearGradient>
        <radialGradient id="panelGlow" cx="0.5" cy="0.6" r="0.6">
          <stop offset="0" stop-color="#4a7bb8"/>
          <stop offset="1" stop-color="#2461a5"/>
        </radialGradient>
      </defs>
      <rect class="portrait-area" x="0" y="0" width="607" height="340" fill="url(#headerGrey)"
            role="img" aria-label="Portrait photograph of Mara Quill against a soft grey studio backdrop"/>
      <path d="M0 250 C 150 320, 330 345, 607 222 L607 818 L0 818 Z" fill="var(--wave-navy)"/>
      <path d="M0 262 C 150 330, 330 350, 607 236 L607 818 L0 818 Z" fill="url(#panelGlow)"/>
    </svg>

    <h2 class="section-label">About Me</h2>
    <h1 class="profile-name">Mara Quill</h1>
    <span class="role-marker" aria-hidden="true"></span>
    <ul class="profile-roles">
      <li>Occupational Therapist</li>
      <li>Coach</li>
      <li>Speaker</li>
    </ul>

    <p class="bio">Mara Quill is the founder and director of Tovil Consulting. She is an occupational therapist, business coach, disability service consultant, speaker and soon to be author. She works with individuals, families, allied health professionals and service providers to design great programmes that achieve brilliant outcomes for people with disabilities.Mara believers that every child is unique and has endless possibilities for growth, regardless of age, stage or diagnosis.</p>
    <p class="invitation">You are invited to contact Mara for further conversation about her services for your child, yourself, your business or organisation.</p>
  </section>

  <section class="address-side">
    <svg class="decor" width="593" height="924" viewBox="0 0 593 924">
      <defs>
        <radialGradient id="decorFade" cx="0.75" cy="0.65" r="0.6">
          <stop offset="0" stop-color="#f0f3f9"/>
          <stop offset="1" stop-color="#ffffff"/>
        </radialGradient>
      </defs>
      <rect x="60" y="260" width="533" height="664" fill="url(#decorFade)"
            role="img" aria-label="Faint large concentric arc decoration"/>
    </svg>
    <div class="stamp-box" aria-label="Stamp area"></div>
    <div class="address-line l1"></div>
    <div class="address-line l2"></div>
    <div class="address-line l3"></div>
  </section>
</main>
</body>
</html>
```